Corvane Partners Web Design

Dear all
I need a web design for a financial services site. We are a broker who deals with many different financial institutions and require a clean, simple and instantly impressive site based on the colour scheme that SketchGuild created for us. A landing page (www.crvnp.mx) gives an idea of the logo and clour scheme but we are looking at either a one page site with rollover text boxes or a 3 or 4 page site depending on the preference of the designer and the best user experience. The site“s purpose is to give confidence that the company exists rather than impart pages of information although we would like this to be a site that can expand over time as the company grows. For now the requirement is for a clear set of possibly changing images at the centre of a white screen that relate to finance in general nad the benefits of wealth creation as well as sectios either along the top or bottom - Our Company, Our Approach, Our services, Our clients, Contact (user to fill in contact box to be sent to info@crvnp.mx. The text for each of these boxes I assume can be added by the coding team here, it the overall look and feel that I am looking for from SketchGuild - deadline can be extended if necessary but I was hoping to wrap this all up in October

Target Market(s)

Succesful individuals looking to maximise returns on their investment via world class financial institutions and supported throughout by qualified independent financial advisors

Industry/Entity Type

Finance

Requirements
Must have
• Logo and color scheme of the logo design SketchGuild sent - I have all these sourcefiles, pantone and fonts

```html
<!DOCTYPE html>
<html lang="en">
<head>
<meta charset="utf-8">
<title>Corvane Partners</title>
<link href="https://fonts.googleapis.com/css2?family=PT+Sans+Narrow:wght@400;700&family=Source+Sans+3:wght@300;400;600&display=swap" rel="stylesheet">
<style>
:root{
  --orange:#fba93a;
  --orange-deep:#f79a1e;
  --ink:#333333;
  --text:#555555;
  --navy:#1d2b4f;
  --footer:#3b3b3b;
  --white:#ffffff;
}
*{box-sizing:border-box;margin:0;padding:0}
html,body{width:959px;height:1200px;overflow:hidden;background:var(--white)}
body{position:relative;font-family:"Source Sans 3",sans-serif;color:var(--text)}
.abs{position:absolute}
.head-font{font-family:"PT Sans Narrow",sans-serif;font-weight:700}

/* header */
.brand{left:92px;top:10px;width:140px;height:78px;text-align:center}
.brand-mark{display:block;width:34px;height:34px;margin:4px auto 6px;border-radius:50%;background:var(--navy)}
.brand-name{font-family:"Source Sans 3",sans-serif;font-weight:400;font-size:13px;letter-spacing:3px;color:var(--navy)}
.quick-contact{right:98px;top:27px;font-size:15px;font-weight:300;color:var(--ink)}
.quick-contact span{color:var(--orange)}
.main-nav{left:309px;top:56px;display:flex;height:44px}
.main-nav a{font-family:"PT Sans Narrow",sans-serif;font-weight:700;font-size:16px;color:var(--ink);text-decoration:none;padding:14px 9px 0;height:44px}
.main-nav a.active{background:var(--orange);color:var(--white);padding:14px 14px 0;margin-right:5px}
.nav-rule{left:0;top:100px;width:959px;height:4px;background:var(--orange)}

/* hero */
.hero{left:0;top:104px;width:959px;height:352px;background:linear-gradient(180deg,#9fc0e0 0%,#cfdfee 45%,#d9b79a 62%,#8cbf55 100%)}
.hero-dots{left:95px;top:420px;display:flex;gap:3px}
.hero-dots i{width:12px;height:12px;border-radius:50%;background:var(--white)}
.hero-dots i:first-child{background:#444}
.contact-form{left:623px;top:137px;width:240px;height:283px;background:rgba(140,170,200,.75);border-radius:3px;padding:0 13px}
.contact-form h2{font-size:17px;color:var(--white);margin:18px 0 12px 3px;font-weight:700}
.field{height:29px;background:rgba(255,255,255,.9);border-radius:3px;margin:0 0 12px 3px;font-size:10px;color:#999;padding:8px 8px}
.field.tall{height:62px}
.submit{left:66px;top:246px;width:99px;height:29px;background:var(--orange);color:var(--white);font-size:16px;text-align:center;line-height:29px}

/* sections */
.section-title{font-size:23px;color:var(--orange)}
.services-title{left:0;width:959px;top:480px;text-align:center}
.service{top:523px;width:240px}
.service .photo{height:122px}
.service h3{font-size:13px;color:var(--ink);margin-top:24px;font-family:"Source Sans 3",sans-serif;font-weight:600}
.service p{font-size:10px;line-height:17.6px;margin-top:12px;text-align:justify;font-weight:300}
.read-more{display:inline-block;margin-top:14px;background:var(--orange);color:var(--white);font-size:12px;padding:3px 7px;font-family:"PT Sans Narrow",sans-serif;font-weight:700}

.about-title{left:104px;top:826px}
.about-photo{left:104px;top:875px;width:431px;height:127px;background:linear-gradient(135deg,#2f4f7a,#a9c8e8 50%,#3a5a80)}
.about-text{left:102px;top:1014px;width:434px;font-size:10px;line-height:17.6px;font-weight:300}
.testi-title{left:552px;top:826px}
.quote{left:552px;width:302px;font-size:10px;line-height:17.6px;font-weight:300;padding-left:14px;text-align:justify}
.quote::before{content:"\201C";position:absolute;left:0;top:-10px;font-size:22px;font-weight:700;color:var(--ink);font-family:Georgia,serif}
.quote .close{font-size:18px;font-weight:700;color:var(--ink);font-family:Georgia,serif;line-height:0}
.quote cite{display:block;font-style:normal;font-weight:600;font-size:12px;color:var(--ink);margin-top:10px}

/* footer */
.footer{left:0;top:1113px;width:959px;height:87px;background:var(--footer)}
.footer-nav{left:101px;top:20px;display:flex;gap:17px}
.footer-nav a{font-family:"PT Sans Narrow",sans-serif;font-weight:700;font-size:13px;color:var(--white);text-decoration:none}
.copyright{left:101px;top:47px;font-size:12px;color:#e6e6e6;font-weight:300}
.social{left:760px;top:28px;display:flex;gap:5px}
.social i{width:28px;height:28px;border-radius:50%}
</style>
</head>
<body>

<header>
  <div class="abs brand"><span class="brand-mark"></span><span class="brand-name">CORVANE PARTNERS</span></div>
  <div class="abs quick-contact"><span>QUICK CONTACT</span> : +52 (55) 2718 4395</div>
  <nav class="abs main-nav">
    <a class="active" href="#">HOME</a><a href="#">OUR COMPANY</a><a href="#">OUR APPROACH</a><a href="#">OUR SERVICES</a><a href="#">OUR CLIENTS</a><a href="#">CONTACT</a>
  </nav>
  <div class="abs nav-rule"></div>
</header>

<section class="abs hero" role="img" aria-label="Cupped hands holding coins with a young green sprout, sky and meadow behind"></section>
<div class="abs hero-dots"><i></i><i></i><i></i><i></i></div>
<form class="abs contact-form">
  <h2 class="head-font">QUICK CONTACT FORM</h2>
  <div class="field">Name</div>
  <div class="field">E-Mail ID</div>
  <div class="field">Phone number</div>
  <div class="field tall">Message</div>
  <div class="abs submit head-font">SUBMIT</div>
</form>

<h2 class="abs section-title head-font services-title">OUR SERVICES</h2>
<article class="abs service" style="left:103px">
  <div class="photo" role="img" aria-label="Businessman balancing on a tightrope above a city" style="background:linear-gradient(180deg,#c9cbcc,#8c8f92)"></div>
  <h3>Risk Management &amp; Compliance</h3>
  <p>Lorem Ipsum is simply dummy text of the printing and typesetting industry. Lorem Ipsum has been the industry's standard dummy text ever since the 1500s, when an unknown printer took a galley ...</p>
  <span class="read-more">READ MORE</span>
</article>
<article class="abs service" style="left:359px">
  <div class="photo" role="img" aria-label="Earth from space with glowing network connections" style="background:radial-gradient(circle at 50% 60%,#3f7bb8,#1a2e55 60%,#05070f)"></div>
  <h3>Global Delivery Network</h3>
  <p>Lorem Ipsum is simply dummy text of the printing and typesetting industry. Lorem Ipsum has been the industry's standard dummy text ever since the 1500s, when an unknown printer took a galley ...</p>
  <span class="read-more">READ MORE</span>
</article>
<article class="abs service" style="left:615px">
  <div class="photo" role="img" aria-label="Hands working on a laptop beside financial charts on a desk" style="background:linear-gradient(135deg,#d8c4a8,#eef0f2 50%,#c9d6e4)"></div>
  <h3>Financial Services Partnerships</h3>
  <p>Lorem Ipsum is simply dummy text of the printing and typesetting industry. Lorem Ipsum has been the industry's standard dummy text ever since the 1500s, when an unknown printer took a galley ...</p>
  <span class="read-more">READ MORE</span>
</article>

<h2 class="abs section-title head-font about-title">ABOUT THE COMPANY</h2>
<div class="abs about-photo" role="img" aria-label="Glass office towers seen from below against a blue sky"></div>
<p class="abs about-text">Lorem Ipsum is simply dummy text of the printing and typesetting industry. Lorem Ipsum has been the industry's standard dummy text ever since the 1500s, when an unknown printer took a galley of type and scrambled it to make a type specimen book. It has survived not only five centuries, but also the leap into electronic typesetting, remaining essentially unchanged.</p>

<h2 class="abs section-title head-font testi-title">TESTIMONIALS</h2>
<blockquote class="abs quote" style="top:880px">Lorem Ipsum is simply dummy text of the printing and typesetting industry. Lorem Ipsum has been the industry's standard dummy text ever since the 1500s, when an unknown printer <span class="close">&#8221;</span>
  <cite>Marcus Ellery</cite></blockquote>
<blockquote class="abs quote" style="top:982px;width:290px">It was popularised in the 1960s with the release of Letrafix sheets containing Loremt Ipsum passages, and more recently with desktop publishing software like Velto PageCraft including versions of Lorem Ipsum. <span class="close">&#8221;</span>
  <cite>Marcus Ellery</cite></blockquote>

<footer class="abs footer">
  <nav class="abs footer-nav"><a href="#">HOME</a><a href="#">OUR COMPANY</a><a href="#">OUR APPROACH</a><a href="#">OUR SERVICES</a><a href="#">OUR CLIENTS</a><a href="#">CONTACT</a></nav>
  <div class="abs copyright">Copyright ©2013&nbsp; Company Name &nbsp;&nbsp; - All rights reserved</div>
  <div class="abs social"><i style="background:#5bc2ea"></i><i style="background:#3b63b0"></i><i style="background:#e0533d"></i></div>
</footer>

</body>
</html>
```